Quillstone Business Card

We need a business card design. We have a logo from a previous Sketchfold project and I am attaching the logo files in jpeg and photoshop.

```html
<!DOCTYPE html>
<html lang="en">
<head>
<meta charset="utf-8">
<title>Quillstone Business Card</title>
<link rel="stylesheet" href="https://fonts.googleapis.com/css2?family=Open+Sans:wght@400;600;700&family=Oswald:wght@500;600&display=swap">
<style>
  :root {
    --green: #5cc31e;
    --ink: #1a1a1a;
    --card-white: #ffffff;
    --card-dark: #3b3b3d;
    --text-grey: #333333;
    --backdrop: #e4e4e4;
  }
  * { box-sizing: border-box; margin: 0; padding: 0; }
  html, body { width: 1200px; height: 900px; overflow: hidden; }
  body {
    background: var(--backdrop);
    font-family: "Open Sans", Arial, sans-serif;
    position: relative;
  }
  .card {
    position: absolute;
    left: 285px;
    width: 630px;
    height: 360px;
    overflow: hidden;
    box-shadow: 0 6px 18px rgba(0,0,0,0.18);
  }
  .card-front { top: 50px; background: var(--card-white); }
  .card-back { top: 470px; background: var(--card-dark); }

  /* front */
  .rule-pair { position: absolute; }
  .rule-pair .rule-green { height: 6px; background: var(--green); }
  .rule-pair .rule-black { height: 3px; background: var(--ink); margin-top: 3px; }
  .rule-top { left: 0; top: 38px; width: 212px; }
  .rule-bottom { right: 0; top: 322px; width: 150px; }

  .identity { position: absolute; left: 226px; top: 20px; }
  .person-name {
    font-family: "Oswald", "Arial Narrow", sans-serif;
    font-weight: 600;
    font-size: 30px;
    letter-spacing: 0.5px;
    color: var(--ink);
    line-height: 1.1;
  }
  .person-title {
    font-size: 9px;
    font-weight: 600;
    letter-spacing: 3.2px;
    color: var(--text-grey);
    margin-top: 4px;
  }

  .contact-list { position: absolute; left: 30px; top: 88px; list-style: none; }
  .contact-item { display: flex; align-items: center; gap: 10px; color: var(--text-grey); margin-bottom: 6px; }
  .contact-item svg { flex: none; }
  .contact-address, .contact-email { font-size: 12px; }
  .contact-phone { font-size: 21px; letter-spacing: 0.5px; }

  .brand-front {
    position: absolute; right: 40px; top: 212px;
    display: flex; align-items: center; gap: 12px;
  }
  .brand-mark { width: 30px; height: 30px; background: var(--green); }
  .brand-name {
    font-weight: 700;
    font-size: 44px;
    color: var(--green);
    letter-spacing: -0.5px;
  }

  .website {
    position: absolute; left: 250px; top: 292px;
    display: flex; align-items: center; gap: 10px;
    font-size: 13px; color: var(--text-grey);
  }

  /* back */
  .stripe { position: absolute; top: 0; width: 5px; height: 100%; background: var(--green); }
  .stripe-one { left: 552px; }
  .stripe-two { left: 566px; }
  .brand-back {
    position: absolute; left: 0; width: 540px; top: 120px;
    display: flex; flex-direction: column; align-items: center;
  }
  .brand-back .brand-row { display: flex; align-items: center; gap: 14px; }
  .brand-back .brand-mark { width: 36px; height: 36px; }
  .brand-back .brand-name { font-size: 52px; }
  .underline { width: 250px; height: 5px; background: var(--green); margin-top: 8px; }
  .underline + .underline { margin-top: 5px; }
</style>
</head>
<body>

<section class="card card-front" aria-label="Business card front">
  <div class="rule-pair rule-top"><div class="rule-green"></div><div class="rule-black"></div></div>

  <div class="identity">
    <h1 class="person-name">DANIEL R. WHITCOMBE II</h1>
    <p class="person-title">CHIEF EXECUTIVE OFFICER</p>
  </div>

  <ul class="contact-list">
    <li class="contact-item contact-address">
      <svg width="16" height="16" viewBox="0 0 16 16" aria-hidden="true"><circle cx="8" cy="8" r="8" fill="var(--green)"/><path d="M4 8.2 8 4.5l4 3.7V12H9.5V9.5h-3V12H4z" fill="#fff"/></svg>
      42 Harrow Lane, Suite 310, Austin, TX 78701
    </li>
    <li class="contact-item contact-phone">
      <svg width="16" height="16" viewBox="0 0 16 16" aria-hidden="true"><circle cx="8" cy="8" r="8" fill="var(--green)"/><rect x="5.5" y="3.5" width="5" height="9" rx="1" fill="#fff"/><rect x="6.5" y="4.8" width="3" height="5.5" fill="var(--green)"/></svg>
      555-014-2290
    </li>
    <li class="contact-item contact-email">
      <svg width="16" height="16" viewBox="0 0 16 16" aria-hidden="true"><circle cx="8" cy="8" r="8" fill="var(--green)"/><rect x="4" y="5" width="8" height="6" fill="#fff"/><path d="M4 5l4 3.3L12 5" fill="none" stroke="var(--green)" stroke-width="1"/></svg>
      dan.whitcombe@quillstonecapital.com
    </li>
  </ul>

  <div class="brand-front">
    <span class="brand-mark"></span>
    <span class="brand-name">Quillstone</span>
  </div>

  <div class="website">
    www.quillstonecapital.com
    <svg width="16" height="16" viewBox="0 0 16 16" aria-hidden="true"><circle cx="8" cy="8" r="8" fill="var(--green)"/><circle cx="8" cy="8" r="4" fill="none" stroke="#fff" stroke-width="1.2"/><path d="M4 8h8M8 4v8" stroke="#fff" stroke-width="1"/></svg>
  </div>

  <div class="rule-pair rule-bottom"><div class="rule-green"></div><div class="rule-black"></div></div>
</section>

<section class="card card-back" aria-label="Business card back">
  <div class="brand-back">
    <div class="brand-row">
      <span class="brand-mark"></span>
      <span class="brand-name">Quillstone</span>
    </div>
    <div class="underline"></div>
    <div class="underline"></div>
  </div>
  <div class="stripe stripe-one"></div>
  <div class="stripe stripe-two"></div>
</section>

</body>
</html>
```